Game Box creation for Kids Classic Games for Outdoor Play

We need to design a game box (soft paper box or carton box) that will contain classic outdoor-old school kids games (teetotums, jumping ropes etc.). I am thinking the design to have a vintage feeling with a modern touch though.
If you come up with some thing different, its welcome..!
The box will have 7 compartments(dividers) inside each representing a game. The Box will have the following dimensions:
60cm(L)x30cm(W)x10cm(H).
Out of the 7 compartments, we need to have one long side divider (compartment) for a ball with its pump (20cm x 30 cm x 10cm) and 6 smaller compartments of 13cm x 15cm x 10cm.
We are thinking - but are not sure - if at the bottom of each compartment (game) there should be a painting/sketch showcasing the game.
We just thought we could call this project "The chest of romps" or "Crate of Frolics" and include as well a small book which will explain how the games are played. Ideas are welcome on the booklet too.
**UPDATE: I have just found an EXCELLENT design that i want to follow. Please see attached and go with it.
Many many thanks!
Target Market(s)
Parents who will remember their youth and the games they played in the neighborhood, hence they will buy for their kids as a gift.
Industry/Entity Type
School
Look and feel

```html
<!DOCTYPE html>
<html lang="en">
<head>
<meta charset="utf-8">
<title>Crate of Frolics – Box Front</title>
<link rel="stylesheet" href="https://fonts.googleapis.com/css2?family=Montserrat:wght@500;800;900&display=swap">
<style>
  :root {
    --stage: #c6e7f0;
    --peach: #f9dfcc;
    --peach-deep: #f2c9ad;
    --blue: #0b8fb8;
    --red: #b5192f;
  }
  html, body {
    margin: 0;
    width: 1200px;
    height: 915px;
    overflow: hidden;
    background: var(--stage);
    font-family: "Montserrat", Arial, sans-serif;
  }
  .box-front {
    position: absolute;
    left: 160px;
    top: 138px;
    width: 880px;
    height: 640px;
    background: var(--peach);
    overflow: hidden;
    box-shadow: 0 18px 40px rgba(40, 90, 110, 0.18);
  }
  .box-front__graphics {
    position: absolute;
    inset: 0;
  }
  .box-title {
    position: absolute;
    left: 150px;
    top: 190px;
    width: 640px;
    margin: 0;
    text-align: center;
    font-weight: 900;
    font-size: 74px;
    line-height: 1;
    color: var(--red);
    text-shadow: -5px 4px 0 var(--blue);
    transform: rotate(-28.6deg);
    transform-origin: center;
    white-space: nowrap;
  }
  .contents-label {
    position: absolute;
    left: 24px;
    top: 560px;
    display: flex;
    align-items: center;
    gap: 12px;
    line-height: 1;
  }
  .contents-label__main {
    font-weight: 800;
    font-size: 44px;
    color: var(--red);
  }
  .contents-label__link {
    font-weight: 500;
    font-size: 27px;
    color: var(--blue);
  }
  .contents-label__stack {
    display: flex;
    flex-direction: column;
    gap: 8px;
  }
  .contents-label__row {
    display: flex;
    align-items: flex-end;
    gap: 10px;
  }
</style>
</head>
<body>
  <section class="box-front">
    <svg class="box-front__graphics" width="880" height="640" viewBox="0 0 880 640">
      <polygon class="sky-band" points="0,0 700,0 0,385" fill="var(--blue)"/>
      <g class="speed-lines" stroke="var(--peach)" stroke-linecap="round">
        <line x1="120" y1="300" x2="640" y2="14" stroke-width="4"/>
        <line x1="60" y1="355" x2="560" y2="80" stroke-width="3"/>
        <line x1="300" y1="170" x2="700" y2="-50" stroke-width="6"/>
      </g>
      <g class="accent-stripes" stroke="var(--blue)">
        <line x1="0" y1="420" x2="763" y2="0" stroke-width="5"/>
        <line x1="0" y1="528" x2="880" y2="44" stroke-width="9"/>
        <line x1="0" y1="548" x2="880" y2="64" stroke-width="3"/>
      </g>
      <circle class="ball-artwork" role="img" aria-label="Outline drawing of a beach ball" cx="580" cy="490" r="112" fill="var(--peach-deep)"/>
      <rect class="pump-artwork" role="img" aria-label="Outline drawing of a hand air pump" x="780" y="265" width="58" height="350" fill="var(--peach-deep)"/>
    </svg>

    <h1 class="box-title">Crate of Frolics</h1>

    <div class="contents-label">
      <span class="contents-label__main">BALL</span>
      <div class="contents-label__stack">
        <span class="contents-label__link">WITH</span>
        <div class="contents-label__row">
          <span class="contents-label__link">ITS</span>
          <span class="contents-label__main">PUMP</span>
        </div>
      </div>
    </div>
  </section>
</body>
</html>
```